Create Lanternfield HR Business Cards.

Create Business Cards for Lanternfield HR. 2 sided and Would like the back to have the logo.

Info for Business Card:
Address: 4827 Millbrook Ave Suite 230 Cleveland, Ohio 44987
Office Number: 216-555-0143
Mobile: 216-555-0192

Website: www.lanternfieldhr.example

Target Market(s)

Small to medium size businesses

Industry/Entity Type

Human Resources

Contact Information for Business Card

Company logo and information

Font styles to use
Serif
Sans Serif

Requirements
Must have
• Info for Business Card: Address: 4827 Millbrook Ave Suite 230 Cleveland, Ohio 44987 Office Number: 216-555-0143 Mobile: 216-555-0192 Website: www.lanternfieldhr.example

```html
<!DOCTYPE html>
<html lang="en">
<head>
<meta charset="utf-8">
<title>Lanternfield HR Business Cards</title>
<link href="https://fonts.googleapis.com/css2?family=Poppins:wght@400;500;600;700&display=swap" rel="stylesheet">
<style>
  :root {
    --stage: #3a3a3a;
    --navy: #262262;
    --navy-deep: #1f1b52;
    --orange: #f7890f;
    --white: #ffffff;
    --rule: #b9b9c4;
  }
  * { box-sizing: border-box; margin: 0; padding: 0; }
  html, body { width: 1200px; height: 689px; overflow: hidden; }
  body {
    background: var(--stage);
    font-family: "Poppins", sans-serif;
    display: flex;
    align-items: center;
    justify-content: center;
    gap: 50px;
  }
  .card {
    width: 525px;
    height: 300px;
    border-radius: 22px;
    border-bottom: 4px solid var(--orange);
    position: relative;
    overflow: hidden;
  }
  .card--back {
    background: var(--navy);
    display: flex;
    align-items: center;
    justify-content: center;
  }
  .card--front {
    background: var(--white);
    display: flex;
    align-items: center;
    padding: 0 30px 0 34px;
  }
  .brand {
    display: flex;
    align-items: center;
    gap: 12px;
    font-weight: 700;
    letter-spacing: 0.5px;
  }
  .brand__dot {
    width: 30px;
    height: 30px;
    border-radius: 50%;
    background: var(--orange);
    flex: none;
  }
  .brand--back .brand__name { color: var(--white); font-size: 32px; }
  .brand--front { width: 205px; }
  .brand--front .brand__name { color: var(--navy); font-size: 22px; line-height: 1.15; }
  .divider {
    width: 1px;
    height: 190px;
    background: var(--rule);
    margin: 0 26px 0 10px;
    flex: none;
  }
  .details { color: var(--navy); }
  .person__name {
    font-size: 19px;
    font-weight: 700;
    text-transform: uppercase;
    letter-spacing: 0.3px;
    line-height: 1.1;
  }
  .person__title {
    font-size: 14px;
    color: var(--orange);
    margin-bottom: 14px;
  }
  .contact { list-style: none; font-size: 12.5px; line-height: 1.2; }
  .contact li { display: flex; align-items: center; gap: 7px; margin-bottom: 5px; }
  .contact__icon {
    width: 15px;
    height: 15px;
    border-radius: 50%;
    background: var(--orange);
    display: flex;
    align-items: center;
    justify-content: center;
    flex: none;
  }
  .contact__icon svg { width: 9px; height: 9px; }
  .accent { color: var(--orange); }
  .address { font-size: 12.5px; line-height: 1.3; margin-top: 12px; }
</style>
</head>
<body>
  <section class="card card--back" aria-label="Card back">
    <div class="brand brand--back">
      <span class="brand__dot"></span>
      <span class="brand__name">Lanternfield HR</span>
    </div>
  </section>

  <section class="card card--front" aria-label="Card front">
    <div class="brand brand--front">
      <span class="brand__dot"></span>
      <span class="brand__name">Lanternfield HR</span>
    </div>
    <div class="divider"></div>
    <div class="details">
      <p class="person__name">Marcus Delaney</p>
      <p class="person__title">Managing Director</p>
      <ul class="contact">
        <li>
          <span class="contact__icon">
            <svg viewBox="0 0 10 10"><path d="M2 1l2 2-1 1c.6 1.3 1.6 2.3 3 3l1-1 2 2-1.5 1.5C4.5 9.3.7 5.5.5 2.5z" fill="#fff"/></svg>
          </span>216-555-0143
        </li>
        <li>
          <span class="contact__icon">
            <svg viewBox="0 0 10 10"><rect x="2.5" y="0.8" width="5" height="8.4" rx="1" fill="none" stroke="#fff" stroke-width="1.2"/></svg>
          </span>216-555-0192
        </li>
        <li>
          <span class="contact__icon">
            <svg viewBox="0 0 10 10" fill="none" stroke="#fff" stroke-width="0.9"><circle cx="5" cy="5" r="4"/><ellipse cx="5" cy="5" rx="1.8" ry="4"/><path d="M1 5h8"/></svg>
          </span>www.<span class="accent">lanternfieldhr</span>.example
        </li>
      </ul>
      <p class="address">4827 Millbrook Ave Suite<br>230 Cleveland, Ohio 44987</p>
    </div>
  </section>
</body>
</html>
```